Orient Wager Digest Quarterly Magazine

We need a magazine design for a new company based in Asia called Orient Wager Digest (OWD).

OWD provide up to date market information for worldwide executives on relevant gaming issues in Asia, covering:
- specific market and legal challenges
- new regulations and their implications for the
industry
- company operations in different jurisdictions (country specific)
- governance and compliance issues
- financing, HR and technology trends

This magazine design must be high-end and relate more to a business periodical/journal that exhibits reliability and industry expertise than a fashion magazine. For reference purpose see Pivotal Magazine and their previous issue. It is important that this design project has synergy with our previous two magazines (see file uploads).

You can also visit http://www.orientwagerdigest.example, however we are in the process of updating this website.

Initially, we would like to see a conceptual SCAMP for 3 spread layouts, including the following pages:

- Main country page template full-spread (text, image, snippet and data/diagram/graph)
- Editorial page
- Contents page
- Sponsors page
- Front Cover

Specific Requirements:
Page Width = 200mm
Page Height = 265mm
Trim measurement = we usually use 5mm
Corporate Colors = Red #990000, Green #226727
Gutter measurement for a 60 page mag, give or take
(*note that most of the odd pages will be Advertising pages consisting of a full page image, therefore they will not need much work.)
Images can bleed off page

Must Haves:
experience in magazine design
able to work with google drive
able to plot graphs, design diagrams, charts etc...

To All,

Logo version has just been uploaded.

Cheers

```html
<!DOCTYPE html>
<html lang="en">
<head>
<meta charset="utf-8">
<title>Orient Wager Digest — Table of Contents Spread</title>
<link rel="stylesheet" href="https://fonts.googleapis.com/css2?family=Open+Sans:wght@300;400&family=Roboto+Slab:wght@300;400;700&family=Playfair+Display:ital@0;1&family=Rokkitt:wght@300;400&display=swap">
<style>
  :root {
    --brand-red: #990000;
    --brand-green: #1fcc1f;
    --ink: #222222;
    --ink-soft: #555555;
    --heading-navy: #0f2d55;
    --paper: #ffffff;
  }
  * { box-sizing: border-box; margin: 0; padding: 0; }
  html, body { width: 1200px; height: 826px; overflow: hidden; background: var(--paper); }
  .spread { position: relative; width: 1200px; height: 826px; }
  .page-left { position: absolute; left: 0; top: 0; width: 577px; height: 826px; background: var(--paper); }
  .page-right { position: absolute; left: 577px; top: 0; width: 623px; height: 826px; background: var(--brand-red); }

  .visual { position: absolute; }
  .visual--mech { left: 2px; top: 46px; width: 286px; height: 215px;
    background: linear-gradient(135deg, #8a8a86 0%, #5d6650 50%, #6c6a62 100%); }
  .visual--arena { left: 2px; top: 368px; width: 527px; height: 184px;
    background: linear-gradient(100deg, #16306b 0%, #2f64c4 45%, #1b2a4a 100%); }
  .visual--space { left: 236px; top: 581px; width: 295px; height: 198px;
    background: linear-gradient(160deg, #2b3a4a 0%, #1a1d24 55%, #6a3b1c 100%); }
  .visual--tower { left: 309px; top: 44px; width: 267px; height: 416px;
    background: linear-gradient(180deg, #1f2630 0%, #2d3037 45%, #7a5420 75%, #2a2620 100%); }

  .toc-title { position: absolute; left: 5px; top: 262px; line-height: 1; }
  .toc-title__line1 { display: block; font-family: "Playfair Display", Georgia, serif; font-size: 52px; color: #111; letter-spacing: 1px; }
  .toc-title__line1 .initial { font-style: italic; font-size: 62px; }
  .toc-title__line2 { display: block; font-family: "Rokkitt", Georgia, serif; font-weight: 300; font-size: 62px; color: var(--heading-navy); margin-top: -6px; letter-spacing: 1px; }

  .entry { position: absolute; width: 240px; }
  .entry__num { position: absolute; left: 0; top: -6px; width: 35px; height: 35px; border-radius: 50%;
    background: var(--brand-green); box-shadow: inset 0 0 0 2px var(--brand-green), inset 0 0 0 3.5px #fff;
    color: #fff; font-family: "Open Sans", Arial, sans-serif; font-weight: 300; font-size: 21px; letter-spacing: -1px;
    display: flex; align-items: center; justify-content: center; }
  .entry__title { margin-left: 42px; font-family: "Open Sans", Arial, sans-serif; font-size: 17.5px; color: var(--ink); line-height: 1.2; }
  .entry__teaser { margin-left: 42px; margin-top: 6px; font-family: "Open Sans", Arial, sans-serif; font-weight: 300; font-size: 12px; line-height: 1.5; color: var(--ink-soft); }
  .page-right .entry__title { color: #fff; }
  .page-right .entry__teaser { color: #f1dede; }

  .masthead { position: absolute; left: 48px; top: 470px; width: 225px; height: 37px; background: #fff;
    display: flex; align-items: center; justify-content: center;
    font-family: "Roboto Slab", Georgia, serif; font-weight: 700; font-size: 16px; color: var(--brand-red); }
  .masthead-rule { position: absolute; left: 273px; top: 484px; width: 350px; height: 8px; background: var(--brand-green); }

  .imprint { position: absolute; top: 523px; width: 175px; font-family: "Roboto Slab", Georgia, serif; font-size: 8.6px; line-height: 16px; color: #fff; font-weight: 300; }
  .imprint strong { font-weight: 700; }
  .imprint--publisher { left: 48px; }
  .imprint--staff { left: 229px; }
  .imprint--events { left: 411px; width: 185px; }
  .imprint__disclaimer { line-height: 10.5px; font-size: 8px; margin-top: 4px; }
</style>
</head>
<body>
<main class="spread">
  <section class="page-left">
    <div class="visual visual--mech" role="img" aria-label="Illustration of an armoured battle mech firing a cannon"></div>

    <div class="entry" style="left:298px; top:53px;"><span class="entry__num">07</span><h2 class="entry__title">LOREM IPSUM</h2><p class="entry__teaser">Lorem ipsum dolor sit amet,</p></div>
    <div class="entry" style="left:298px; top:116px;"><span class="entry__num">08</span><h2 class="entry__title">LOREM IPSUM</h2><p class="entry__teaser">consectetuer adipiscing elit.<br>Aenean commodo ligula eget</p></div>
    <div class="entry" style="left:298px; top:188px;"><span class="entry__num">11</span><h2 class="entry__title">LOREM IPSUM</h2><p class="entry__teaser">dolor. Aenean massa. Cum sociis</p></div>
    <div class="entry" style="left:298px; top:255px;"><span class="entry__num">13</span><h2 class="entry__title">LOREM IPSUM</h2><p class="entry__teaser">natoque penatibus et magnis dis</p></div>
    <div class="entry" style="left:298px; top:315px;"><span class="entry__num">14</span><h2 class="entry__title">LOREM IPSUM</h2><p class="entry__teaser">parturient montes, nascetur</p></div>

    <h1 class="toc-title"><span class="toc-title__line1"><span class="initial">T</span>able of</span><span class="toc-title__line2">contents</span></h1>

    <div class="visual visual--arena" role="img" aria-label="Photo of an esports player with headphones at a tournament computer station"></div>

    <div class="entry" style="left:2px; top:575px;"><span class="entry__num">24</span><h2 class="entry__title">LOREM IPSUM</h2><p class="entry__teaser">ridiculus mus. Donec quam felis,</p></div>
    <div class="entry" style="left:2px; top:638px;"><span class="entry__num">28</span><h2 class="entry__title">LOREM IPSUM</h2><p class="entry__teaser">ultricies nec, pellentesque eu,<br>pretium quis, sem. Nulla</p></div>
    <div class="entry" style="left:2px; top:711px;"><span class="entry__num">31</span><h2 class="entry__title">LOREM IPSUM</h2><p class="entry__teaser">consequat massa quis enim.<br>Donec pede justo, fringilla vel,</p></div>

    <div class="visual visual--space" role="img" aria-label="Science fiction artwork of an armoured space suit overlooking a ruined city"></div>
  </section>

  <section class="page-right">
    <div class="entry" style="left:55px; top:64px;"><span class="entry__num">38</span><h2 class="entry__title">LOREM IPSUM</h2><p class="entry__teaser">Lorem ipsum dolor sit amet,</p></div>
    <div class="entry" style="left:55px; top:126px;"><span class="entry__num">45</span><h2 class="entry__title">LOREM IPSUM</h2><p class="entry__teaser">consectetuer adipiscing elit.<br>Aenean commodo ligula eget</p></div>
    <div class="entry" style="left:55px; top:200px;"><span class="entry__num">49</span><h2 class="entry__title">LOREM IPSUM</h2><p class="entry__teaser">Lorem ipsum dolor sit amet,</p></div>
    <div class="entry" style="left:55px; top:262px;"><span class="entry__num">53</span><h2 class="entry__title">LOREM IPSUM</h2><p class="entry__teaser">consectetuer adipiscing elit.<br>Aenean commodo ligula eget</p></div>
    <div class="entry" style="left:55px; top:337px;"><span class="entry__num">57</span><h2 class="entry__title">LOREM IPSUM</h2><p class="entry__teaser">Lorem ipsum dolor sit amet,</p></div>
    <div class="entry" style="left:55px; top:398px;"><span class="entry__num">58</span><h2 class="entry__title">LOREM IPSUM</h2><p class="entry__teaser">consectetuer adipiscing elit.<br>Aenean commodo ligula eget</p></div>

    <div class="visual visual--tower" role="img" aria-label="Night photo of an illuminated lattice tower above a city skyline"></div>

    <div class="masthead">Orient Wager Digest</div>
    <div class="masthead-rule"></div>

    <div class="imprint imprint--publisher">
      <strong>Published by: Harbour Kite Media Ltd.</strong><br>
      Suite 802 - 8/ F,<br>
      Lotus Bay Business Tower<br>
      215 Rua da Lanterna Azul<br>
      Macau SAR<br>
      P.O. Box 4702<br>
      t. +853 2000 0481<br>
      f. +853 2000 0482<br>
      e. enquiries@owdigest.example<br>
      <strong>advertising enquiries:</strong><br>
      advertising@owdigest.example<br>
      <strong>subscription enquiries:</strong><br>
      sub@owdigest.example
    </div>
    <div class="imprint imprint--staff">
      <strong>editorial enquiries:</strong><br>
      editorial@owdigest.example<br>
      <strong>Publishers &amp; MDs</strong><br>
      Marina Holt<br>
      Tomas Avelar<br>
      <strong>Managing Editor</strong><br>
      Tomas Avelar<br>
      Research Analyst<br>
      Irene Castell<br>
      <strong>Design</strong><br>
      Northgrid Studio Ltd.<br>
      <strong>Photography</strong><br>
      Pearl Lens, Agencies<br>
      <strong>Printing</strong><br>
      Kin Wah Press, Hong Kong
    </div>
    <div class="imprint imprint--events">
      <strong>OWD events</strong><br>
      Crest Gaming Forum<br>
      Summit Play Asia<br>
      Eastern Steppe Gaming Week<br>
      Southern Cross Gaming Expo<br>
      Summit Play Nevada<br>
      Pearl River Gaming Show<br>
      www.orientwagerdigest.example<br>
      <strong>DISCLAIMER:</strong>
      <p class="imprint__disclaimer">All rights reserved. No part of this publication may be reproduced or transmitted in any shape or form, or by any means, or stored in any retrieval system of any nature, without prior express permission. The publishers accept no responsibility for loss or damage to any materials submitted for publication. The views expressed within are not necessarily subscribed by the</p>
    </div>
  </section>
</main>
</body>
</html>
```